Website design for labour force (commercial truck driver) company

Looking for a Wordpress template (or design files in conjunction with a free Wordpress template).
Company tag line:
CargoLoop – On Demand, Professional Drivers
Real Drivers | Real Standards | Real Results
Logo design has already been completed and is attached

Company provides contract drivers to trucking companies. Target market is both the trucking companies looking for drivers and drivers looking for work.
Design to encompass header / footer and basic page design, navigation menu, home page, contact page. Customer will add content and additional pages over time.

```html
<!DOCTYPE html>
<html lang="en">
<head>
<meta charset="utf-8">
<title>CargoLoop – On Demand, Professional Drivers</title>
<link href="https://fonts.googleapis.com/css2?family=Poppins:wght@500;600;700&family=Roboto:wght@400;500;700&display=swap" rel="stylesheet">
<style>
:root{
  --green:#0c8a63;
  --green-dark:#06573f;
  --black:#000;
  --ink:#111;
  --white:#fff;
  --muted:#d9d9d9;
}
*{box-sizing:border-box;margin:0;padding:0}
html,body{width:1200px;height:3628px;overflow:hidden}
body{font-family:"Roboto",Arial,sans-serif;color:var(--white);background:var(--black);position:relative}
.section{position:absolute;left:0;width:1200px}
a{color:inherit;text-decoration:none}

/* top bar */
.topbar{top:0;height:64px;background:var(--black);display:flex;align-items:center;justify-content:flex-end;gap:48px;padding-right:56px;font-size:15px;font-weight:500}
.topbar .item{display:flex;align-items:center;gap:10px}
.topbar .socials{display:flex;gap:10px}
.dot{width:22px;height:22px;border-radius:50%;background:var(--white);display:inline-block}

/* header */
.header{top:64px;height:168px;background:var(--white);display:flex;align-items:center;justify-content:space-between;padding:0 60px 0 48px}
.brand{display:flex;align-items:center;gap:16px;font-family:"Poppins",Arial,sans-serif;font-weight:700;font-size:46px;color:var(--ink)}
.brand .mark{width:44px;height:44px;border-radius:50%;background:var(--green)}
.nav{display:flex;align-items:center;gap:58px;height:72px;padding:0 42px;background:var(--green);border-radius:36px;box-shadow:0 0 0 4px var(--white),0 0 0 7px var(--green);font-family:"Poppins",Arial,sans-serif;font-weight:600;font-size:22px;letter-spacing:1px;color:var(--white)}

/* hero */
.hero{top:232px;height:868px;background:linear-gradient(180deg,#c6d8e6 0%,#e4eaec 40%,#a9ab8f 58%,#6f7d4e 78%,#4a5633 100%)}
.hero-text{position:absolute;left:0;width:1200px;top:578px;text-align:center;text-shadow:0 2px 6px rgba(0,0,0,.5)}
.hero-text .kicker{font-family:"Poppins",Arial,sans-serif;font-weight:600;font-size:30px;letter-spacing:2px}
.hero-text h1{font-family:"Poppins",Arial,sans-serif;font-weight:600;font-size:33px;letter-spacing:1px;margin-top:2px}
.btn-dark{display:inline-block;margin-top:44px;background:var(--black);color:var(--white);padding:18px 42px;border-radius:30px;font-size:22px;font-weight:500;text-shadow:none}

/* services */
.services{top:1100px;height:796px;background:var(--black)}
.section-title{font-family:"Poppins",Arial,sans-serif;font-weight:600;font-size:34px;letter-spacing:2px;text-align:center}
.services .section-title{margin-top:84px}
.service-row{display:flex;justify-content:space-between;padding:0 56px;margin-top:72px}
.service{width:312px;text-align:center}
.service svg{display:block;margin:0 auto}
.pill{margin-top:38px;height:54px;background:var(--green);border-radius:27px;display:flex;align-items:center;justify-content:center;position:relative;font-family:"Poppins",Arial,sans-serif;font-weight:600;font-size:24px;letter-spacing:1px}
.pill::before{content:"";position:absolute;left:0;top:0;width:60px;height:54px;border-radius:27px 0 0 27px;background:var(--green-dark)}
.pill span{position:relative}
.service p{margin-top:40px;font-size:20px;line-height:31px;font-weight:500;letter-spacing:.5px;white-space:nowrap}
.btn-outline{display:inline-block;margin-top:30px;border:3px solid var(--white);padding:10px 22px;font-size:22px;font-weight:500;letter-spacing:1px}

/* testimonials */
.testi-band{top:1896px;height:80px;background:var(--green);display:flex;align-items:center;justify-content:center}
.testimonials{top:1976px;height:572px;background:var(--white)}
.cards{display:flex;justify-content:space-between;padding:36px 60px 0}
.card{width:320px;height:456px;background:var(--white);box-shadow:0 3px 14px rgba(0,0,0,.18);border-radius:6px;padding:8px;color:var(--ink)}
.card .photo{height:200px;border-radius:6px;border:2px solid #555}
.card h3{margin:24px 10px 0;font-size:15px;font-weight:700}
.card p{margin:12px 10px 0;font-size:14px;line-height:20px;color:#333;white-space:nowrap}
.card .actions{display:flex;align-items:center;margin:22px 10px 0;gap:12px}
.btn-pill{background:var(--black);color:var(--white);font-size:16px;font-weight:700;padding:9px 22px;border-radius:18px;margin-right:auto}
.icon-circle{width:32px;height:32px;border-radius:50%;background:#eee;display:flex;align-items:center;justify-content:center}

/* contact */
.contact{top:2548px;height:612px;background:linear-gradient(180deg,#101214 0%,#23272b 45%,#3a3d40 62%,#121416 100%)}
.contact .section-title{margin-top:62px;font-size:34px}
.form{position:absolute;left:60px;top:150px;width:1080px;font-size:21px;font-weight:500}
.field{position:absolute;border-bottom:3px solid var(--white);padding-bottom:12px}
.submit{position:absolute;left:460px;top:330px;width:168px;height:54px;background:var(--green);border-radius:4px 22px 4px 22px;display:flex;align-items:center;justify-content:center;font-size:26px;font-weight:700;letter-spacing:1px}

/* footer */
.footer{top:3160px;height:468px;background:var(--black)}
.footer .brand{position:absolute;left:48px;top:56px;color:var(--white);font-size:42px}
.footer .about{position:absolute;left:48px;top:152px;font-size:19px;line-height:28px;font-weight:500}
.footer .follow{position:absolute;left:48px;top:272px;font-size:18px;font-weight:700;letter-spacing:1px}
.footer .fsocial{position:absolute;left:48px;top:324px;display:flex;gap:26px}
.footer .fsocial .dot{width:30px;height:30px;background:none;border:3px solid var(--white)}
.col{position:absolute;top:62px}
.col h4{font-size:20px;font-weight:700;letter-spacing:1px;margin-bottom:22px}
.col li{list-style:none;font-size:16px;font-weight:500;margin-bottom:20px}
.col .c-item{display:flex;align-items:center;gap:14px;font-size:16px;font-weight:500;margin-bottom:30px}
.copyright{position:absolute;left:400px;top:362px;font-size:16px;font-weight:500}
</style>
</head>
<body>

<div class="section topbar">
  <div class="item">
    <svg width="18" height="18" viewBox="0 0 24 24"><path fill="#fff" d="M6.6 10.8a15 15 0 0 0 6.6 6.6l2.2-2.2a1 1 0 0 1 1-.25 11.4 11.4 0 0 0 3.6.57 1 1 0 0 1 1 1V20a1 1 0 0 1-1 1A17 17 0 0 1 3 4a1 1 0 0 1 1-1h3.5a1 1 0 0 1 1 1c0 1.25.2 2.45.57 3.6a1 1 0 0 1-.25 1z"/></svg>
    <span>Call now: +0000000000</span>
  </div>
  <div class="item">
    <svg width="20" height="16" viewBox="0 0 20 16"><rect width="20" height="16" rx="2" fill="#fff"/><path d="M1 2l9 7 9-7" stroke="#000" stroke-width="2" fill="none"/></svg>
    <span>Email info: yourcompany@address.com</span>
  </div>
  <div class="socials"><span class="dot"></span><span class="dot"></span><span class="dot"></span><span class="dot"></span></div>
</div>

<header class="section header">
  <div class="brand"><span class="mark"></span>CargoLoop</div>
  <nav class="nav"><a>HOME</a><a>SERVICES</a><a>BOOKING</a><a>CONTACT US</a></nav>
</header>

<section class="section hero" role="img" aria-label="White truck driving on a countryside highway at sunrise beside green fields">
  <div class="hero-text">
    <div class="kicker">WELCOME TO</div>
    <h1>CargoLoop – On Demand, Professional Drivers</h1>
    <a class="btn-dark">Get Started</a>
  </div>
</section>

<section class="section services">
  <h2 class="section-title">OUR SERVICES</h2>
  <div class="service-row">
    <div class="service">
      <svg width="112" height="64" viewBox="0 0 112 64"><rect x="0" y="0" width="70" height="48" fill="#fff"/><path d="M74 14h22l14 18v16H74z" fill="#fff"/><circle cx="22" cy="54" r="9" fill="#fff" stroke="#000" stroke-width="3"/><circle cx="92" cy="54" r="9" fill="#fff" stroke="#000" stroke-width="3"/></svg>
      <div class="pill"><span>LOREM IPSUM</span></div>
      <p>Lorem ipsum dolor sit amet,<br>consectetur adipiscing elit,<br>sed do eiusmod tempor<br>incididunt ut labore</p>
      <a class="btn-outline">read more</a>
    </div>
    <div class="service">
      <svg width="112" height="64" viewBox="0 0 112 64"><rect x="0" y="0" width="70" height="48" fill="#fff"/><path d="M74 14h22l14 18v16H74z" fill="#fff"/><circle cx="22" cy="54" r="9" fill="#fff" stroke="#000" stroke-width="3"/><circle cx="92" cy="54" r="9" fill="#fff" stroke="#000" stroke-width="3"/></svg>
      <div class="pill"><span>LOREM IPSUM</span></div>
      <p>Lorem ipsum dolor sit amet,<br>consectetur adipiscing elit,<br>sed do eiusmod tempor<br>incididunt ut labore</p>
      <a class="btn-outline">read more</a>
    </div>
    <div class="service">
      <svg width="112" height="64" viewBox="0 0 112 64"><rect x="0" y="0" width="70" height="48" fill="#fff"/><path d="M74 14h22l14 18v16H74z" fill="#fff"/><circle cx="22" cy="54" r="9" fill="#fff" stroke="#000" stroke-width="3"/><circle cx="92" cy="54" r="9" fill="#fff" stroke="#000" stroke-width="3"/></svg>
      <div class="pill"><span>LOREM IPSUM</span></div>
      <p>Lorem ipsum dolor sit amet,<br>consectetur adipiscing elit,<br>sed do eiusmod tempor<br>incididunt ut labore</p>
      <a class="btn-outline">read more</a>
    </div>
  </div>
</section>

<div class="section testi-band"><h2 class="section-title">CUSTOMER TESTIMONIALS</h2></div>

<section class="section testimonials">
  <div class="cards">
    <article class="card">
      <div class="photo" role="img" aria-label="Smiling truck driver standing in front of his truck" style="background:linear-gradient(135deg,#b9a58a,#6e5a48 60%,#d6c7ae)"></div>
      <h3>LOREM IPSUM DOLOR SIT AMET</h3>
      <p>Lorem ipsum dolor sited consectetur<br>adipiscing elited sed eiusmod<br>tempor incididunt ut labore et<br>dolore magna aliqua.</p>
      <div class="actions"><a class="btn-pill">read more</a>
        <span class="icon-circle"><svg width="14" height="14" viewBox="0 0 14 14"><circle cx="3" cy="7" r="2" fill="#111"/><circle cx="11" cy="3" r="2" fill="#111"/><circle cx="11" cy="11" r="2" fill="#111"/><path d="M3 7L11 3M3 7l8 4" stroke="#111" stroke-width="1.3"/></svg></span>
        <span class="icon-circle"><svg width="14" height="13" viewBox="0 0 14 13"><path d="M7 12L1.5 6.5A3 3 0 0 1 7 2.5a3 3 0 0 1 5.5 4z" fill="#111"/></svg></span>
      </div>
    </article>
    <article class="card">
      <div class="photo" role="img" aria-label="Driver waving from the cab window of a truck" style="background:linear-gradient(135deg,#d9d7cf,#7b6b5a 55%,#b8b3a6)"></div>
      <h3>LOREM IPSUM DOLOR SIT AMET</h3>
      <p>Lorem ipsum dolor sited consectetur<br>adipiscing elited sed eiusmod<br>tempor incididunt ut labore et<br>dolore magna aliqua.</p>
      <div class="actions"><a class="btn-pill">read more</a>
        <span class="icon-circle"><svg width="14" height="14" viewBox="0 0 14 14"><circle cx="3" cy="7" r="2" fill="#111"/><circle cx="11" cy="3" r="2" fill="#111"/><circle cx="11" cy="11" r="2" fill="#111"/><path d="M3 7L11 3M3 7l8 4" stroke="#111" stroke-width="1.3"/></svg></span>
        <span class="icon-circle"><svg width="14" height="13" viewBox="0 0 14 13"><path d="M7 12L1.5 6.5A3 3 0 0 1 7 2.5a3 3 0 0 1 5.5 4z" fill="#111"/></svg></span>
      </div>
    </article>
    <article class="card">
      <div class="photo" role="img" aria-label="Driver seated at the wheel inside a truck cab" style="background:linear-gradient(135deg,#4d7fb5,#8a5a3e 55%,#2f5f94)"></div>
      <h3>LOREM IPSUM DOLOR SIT AMET</h3>
      <p>Lorem ipsum dolor sited consectetur<br>adipiscing elited sed eiusmod<br>tempor incididunt ut labore et<br>dolore magna aliqua.</p>
      <div class="actions"><a class="btn-pill">read more</a>
        <span class="icon-circle"><svg width="14" height="14" viewBox="0 0 14 14"><circle cx="3" cy="7" r="2" fill="#111"/><circle cx="11" cy="3" r="2" fill="#111"/><circle cx="11" cy="11" r="2" fill="#111"/><path d="M3 7L11 3M3 7l8 4" stroke="#111" stroke-width="1.3"/></svg></span>
        <span class="icon-circle"><svg width="14" height="13" viewBox="0 0 14 13"><path d="M7 12L1.5 6.5A3 3 0 0 1 7 2.5a3 3 0 0 1 5.5 4z" fill="#111"/></svg></span>
      </div>
    </article>
  </div>
</section>

<section class="section contact" role="img" aria-label="Dark background of a truck driving on a highway at night">
  <h2 class="section-title">GET IN TOUCH</h2>
  <div class="form">
    <div class="field" style="left:0;top:0;width:460px">First Name:</div>
    <div class="field" style="left:640px;top:0;width:440px">Last Name:</div>
    <div class="field" style="left:0;top:110px;width:460px">Email address:</div>
    <div class="field" style="left:640px;top:110px;width:440px">Phone number:</div>
    <div class="field" style="left:0;top:218px;width:1080px">Messages:</div>
    <div class="submit">Submit</div>
  </div>
</section>

<footer class="section footer">
  <div class="brand"><span class="mark"></span>CargoLoop</div>
  <p class="about">Lorem ipsum dolor sit amet,<br>consectetur adipiscing elit</p>
  <div class="follow">FOLLOW ON</div>
  <div class="fsocial"><span class="dot"></span><span class="dot"></span><span class="dot"></span><span class="dot"></span></div>
  <div class="col" style="left:432px">
    <h4>QUICKLINKS</h4>
    <ul><li>&gt;&gt; Home</li><li>&gt;&gt; About Us</li><li>&gt;&gt; Services</li><li>&gt;&gt; News</li><li>&gt;&gt; Contact Us</li></ul>
  </div>
  <div class="col" style="left:628px">
    <h4>OTHERLINKS</h4>
    <ul><li>&gt;&gt; Team</li><li>&gt;&gt; FAQ</li><li>&gt;&gt; Services</li><li>&gt;&gt; Privacy</li><li>&gt;&gt; Policy</li></ul>
  </div>
  <div class="col" style="left:816px">
    <h4>CONTACT US</h4>
    <div class="c-item"><svg width="18" height="18" viewBox="0 0 24 24"><path fill="#fff" d="M6.6 10.8a15 15 0 0 0 6.6 6.6l2.2-2.2a1 1 0 0 1 1-.25 11.4 11.4 0 0 0 3.6.57 1 1 0 0 1 1 1V20a1 1 0 0 1-1 1A17 17 0 0 1 3 4a1 1 0 0 1 1-1h3.5a1 1 0 0 1 1 1c0 1.25.2 2.450.57 3.6a1 1 0 0 1-.25 1z"/></svg>Call now: +0000000000</div>
    <div class="c-item"><svg width="20" height="16" viewBox="0 0 20 16"><rect width="20" height="16" rx="2" fill="#fff"/><path d="M1 2l9 7 9-7" stroke="#000" stroke-width="2" fill="none"/></svg>Email: company@address.com</div>
  </div>
  <div class="copyright">© Copyrights 2025 CargoLoop All Rights Reserved</div>
</footer>

</body>
</html>
```